COMPANY SIGN AND SHOWCASE DESIGN

I need the design of the sign for our company's corporate offices, attached is a photo of the previous business that was called Corvanta, now we are in that location, IN THE PHOTO FROM THE STREET with the number 1 in yellow I have put where I need to design a sign or sign, this sign can be lit up at night and in 2 also in yellow is the shop window that we must also design with ideas.

I also attach the BRANDBOOK of our brand AMBER AND SAND HOUSES, we are a company dedicated to the tourist rental of villas in Ibiza and Menorca.

The company is dedicated to the tourist management of licensed tourist homes in Ibiza, so we want the shop window and the sign to indicate the name of the brand, its logo and also to make it clear that it is this office.

We want to attract the attention of people passing by on the street and make them understand what we do. We are NOT a real estate agency but rather a tourist company that manages holiday homes or villas.

Target Market(s)

People passing by on the street and seeing our illuminated sign and the shop window at street level

Industry/Entity Type

Turismo, ALQUILER TURÍSTICO DE VILLAS

Requirements
Must have
• BRAND BOOK ATTACHED
Nice to have
• BRAND BOOK ATTACHED
Should not have
• BRAND BOOK ATTACHED

```html
<!DOCTYPE html>
<html lang="en">
<head>
<meta charset="utf-8">
<title>Amber &amp; Sand – Storefront Sign and Window</title>
<link rel="stylesheet" href="https://fonts.googleapis.com/css2?family=Exo+2:wght@400;500;600;700&family=Inter:wght@400;500&display=swap">
<style>
  :root{
    --frame:#000000;
    --navy:#0f5a7d;
    --navy-deep:#0b4e6e;
    --lime:#8ac65a;
    --teal:#2f9ab6;
    --icon-ring:#0e4d77;
    --slate:#4a4b4d;
    --slate-dark:#39393b;
    --white:#ffffff;
  }
  *{margin:0;padding:0;box-sizing:border-box;}
  html,body{width:1200px;height:900px;overflow:hidden;background:var(--white);}
  body{position:relative;font-family:"Exo 2",sans-serif;color:var(--white);}

  .storefront{position:absolute;left:39px;top:61px;width:1113px;height:791px;background:var(--frame);}

  .fascia{position:absolute;left:53px;top:32px;width:1022px;height:190px;
    background:linear-gradient(100deg,var(--navy-deep),var(--navy) 55%,#146489);
    text-align:center;}
  .fascia__name{position:absolute;left:0;right:0;top:38px;font-size:82px;font-weight:600;
    letter-spacing:2px;color:var(--lime);line-height:1;}
  .fascia__tagline{position:absolute;left:0;right:0;top:133px;font-family:"Inter",sans-serif;
    font-size:26px;letter-spacing:8px;font-weight:500;}
  .fascia__tagline .dot{color:var(--lime);}

  .pane{position:absolute;overflow:hidden;}
  .pane__bg{position:absolute;inset:0;background:linear-gradient(170deg,var(--slate),var(--slate-dark));}

  .pane--rentals{left:54px;top:255px;width:304px;height:510px;}
  .pane--door{left:403px;top:268px;width:171px;height:490px;}
  .pane--monogram{left:615px;top:268px;width:162px;height:490px;}
  .pane--discover{left:819px;top:256px;width:226px;height:502px;}

  .headline{position:absolute;left:0;right:0;text-align:center;font-weight:600;}
  .pane--rentals .headline{top:36px;font-size:50px;line-height:.95;letter-spacing:-1px;}
  .pane--discover .headline{top:20px;font-size:33px;line-height:1;font-weight:500;}

  .pool-photo{position:absolute;left:0;right:0;top:171px;height:206px;
    background:linear-gradient(180deg,#35a0bb 0%,#3aa4bf 25%,#c8b48c 45%,#4f9ad0 60%,#c9b790 78%,#4c7c3a 100%);}
  .badge{position:absolute;left:98px;top:146px;width:104px;height:104px;border-radius:50%;
    background:var(--lime);border:3px solid var(--white);display:flex;align-items:center;justify-content:center;
    text-align:center;font-size:15px;font-weight:500;line-height:1.2;}

  .web-band{position:absolute;left:0;right:0;top:377px;height:42px;background:var(--lime);
    display:flex;align-items:center;justify-content:center;gap:6px;font-size:19px;font-weight:500;}
  .pane--discover .web-band{font-size:16px;}

  .phone{position:absolute;left:0;right:0;display:flex;align-items:center;justify-content:center;
    gap:6px;font-weight:500;line-height:1;}
  .pane--rentals .phone{top:433px;height:34px;font-size:28px;}
  .pane--discover .phone{top:436px;height:28px;font-size:22px;}

  .door-brand{position:absolute;left:0;right:0;top:64px;text-align:center;font-size:30px;font-weight:600;line-height:1;letter-spacing:1px;}
  .door-sub{position:absolute;left:0;right:0;text-align:center;font-family:"Inter",sans-serif;letter-spacing:4px;font-size:16px;}
  .door-sub--villas{top:142px;color:var(--lime);}
  .door-sub--menorca{top:176px;}
  .door-sub--ibiza{top:202px;}
  .door-handle{position:absolute;left:136px;top:216px;width:35px;height:101px;border:9px solid var(--frame);border-right:none;}
  .door-phone{position:absolute;left:0;right:0;top:347px;text-align:center;font-size:18px;font-weight:500;}
  .door-rule{position:absolute;left:23px;right:23px;top:370px;height:18px;display:flex;align-items:center;gap:5px;}
  .door-rule span{flex:1;height:1px;background:var(--white);opacity:.8;}
  .door-hours{position:absolute;left:0;right:0;top:390px;text-align:center;font-size:16px;font-weight:500;}

  .monogram{position:absolute;left:0;right:0;top:30px;text-align:center;font-weight:600;color:var(--lime);
    font-size:138px;line-height:.95;}

  .features{position:absolute;left:0;right:0;top:171px;height:206px;background:var(--teal);
    display:grid;grid-template-columns:1fr 1fr;padding:16px 8px 10px;row-gap:6px;}
  .feature{display:flex;flex-direction:column;align-items:center;text-align:center;font-size:11px;font-weight:500;line-height:1.15;}
  .feature svg{margin-bottom:6px;}
</style>
</head>
<body>
<main class="storefront">

  <header class="fascia">
    <div class="fascia__name">AMBER &amp; SAND</div>
    <div class="fascia__tagline"><span class="dot">•</span> MENORCA <span class="dot">•</span> IBIZA VILLAS</div>
  </header>

  <section class="pane pane--rentals">
    <div class="pane__bg" role="img" aria-label="Muted grey office interior"></div>
    <h2 class="headline">VACATION<br>RENTALS</h2>
    <div class="pool-photo" role="img" aria-label="Aerial view of a villa pool with sun loungers and lawn"></div>
    <div class="badge">LICENSED<br>TOURIST<br>HOMES</div>
    <div class="web-band">
      <svg width="18" height="18" viewBox="0 0 20 20" fill="none" stroke="#fff" stroke-width="1.6"><circle cx="10" cy="10" r="8.5"/><ellipse cx="10" cy="10" rx="3.8" ry="8.5"/><path d="M1.5 10h17"/></svg>
      amberandsandstays.com
    </div>
    <div class="phone">
      <svg width="22" height="22" viewBox="0 0 24 24" fill="none" stroke="#fff" stroke-width="2"><path d="M5 3h4l2 5-2.5 1.5a11 11 0 0 0 6 6L16 13l5 2v4a2 2 0 0 1-2 2A17 17 0 0 1 3 5a2 2 0 0 1 2-2z"/></svg>
      34 600 481 372
    </div>
  </section>

  <section class="pane pane--door">
    <div class="pane__bg" role="img" aria-label="Muted grey office corridor seen through the glass door"></div>
    <div class="door-brand">AMBER<br>&amp; SAND</div>
    <div class="door-sub door-sub--villas">VILLAS</div>
    <div class="door-sub door-sub--menorca">MENORCA</div>
    <div class="door-sub door-sub--ibiza">IBIZA</div>
    <div class="door-handle"></div>
    <div class="door-phone">34 600 481 372</div>
    <div class="door-rule"><span></span>
      <svg width="18" height="18" viewBox="0 0 20 20"><circle cx="10" cy="10" r="9" fill="var(--lime)"/><path d="M7 5h2l1 3-1.3.8a5.5 5.5 0 0 0 2.5 2.5L12 10l3 1v2a1 1 0 0 1-1 1A8.5 8.5 0 0 1 6 6a1 1 0 0 1 1-1z" fill="none" stroke="#fff" stroke-width="1.2"/></svg>
      <span></span></div>
    <div class="door-hours">9:00h - 21:00h</div>
  </section>

  <section class="pane pane--monogram">
    <div class="pane__bg" role="img" aria-label="Muted grey office workspace with desks and chairs"></div>
    <div class="monogram">A<br>&amp;<br>S</div>
  </section>

  <section class="pane pane--discover">
    <div class="pane__bg" role="img" aria-label="Muted grey office interior"></div>
    <h2 class="headline">Discover<br>paradise in<br>one of our<br>dream villas</h2>
    <div class="features">
      <div class="feature">
        <svg width="48" height="48" viewBox="0 0 48 48" fill="none" stroke="#fff" stroke-width="1.6"><circle cx="24" cy="24" r="23" fill="var(--icon-ring)" stroke="#fff"/><path d="M24 13l9 3v7c0 6-4 10-9 12-5-2-9-6-9-12v-7z"/><path d="M20 24l3 3 5-6"/></svg>
        EXCLUSIVITY<br>AND PRIVACY
      </div>
      <div class="feature">
        <svg width="48" height="48" viewBox="0 0 48 48" fill="none" stroke="#fff" stroke-width="1.6"><circle cx="24" cy="24" r="23" fill="var(--icon-ring)" stroke="#fff"/><path d="M24 36s-9-9-9-15a9 9 0 0 1 18 0c0 6-9 15-9 15z"/><circle cx="24" cy="21" r="3.5"/></svg>
        PRIME<br>LOCATION
      </div>
      <div class="feature">
        <svg width="48" height="48" viewBox="0 0 48 48" fill="none" stroke="#fff" stroke-width="1.6"><circle cx="24" cy="24" r="23" fill="var(--icon-ring)" stroke="#fff"/><path d="M13 34V22l8-6v18M21 34h14V25l-7-5"/><path d="M25 28h3v6M31 28h2"/></svg>
        DESIGN AND<br>ARCHITECTURE
      </div>
      <div class="feature">
        <svg width="48" height="48" viewBox="0 0 48 48" fill="none" stroke="#fff" stroke-width="1.6"><circle cx="24" cy="24" r="23" fill="var(--icon-ring)" stroke="#fff"/><circle cx="18" cy="19" r="3.5"/><path d="M18 12v2M18 24v2M11 19h2M23 19h2"/><path d="M12 32c3-2 5-2 8 0s5 2 8 0 5-2 8 0"/><path d="M28 29v-12M23 20a5 4 0 0 1 10 0z"/></svg>
        LUXURIOUS<br>FACILITIES
      </div>
    </div>
    <div class="web-band">
      <svg width="15" height="15" viewBox="0 0 20 20" fill="none" stroke="#fff" stroke-width="1.6"><circle cx="10" cy="10" r="8.5"/><ellipse cx="10" cy="10" rx="3.8" ry="8.5"/><path d="M1.5 10h17"/></svg>
      amberandsandstays.com
    </div>
    <div class="phone">
      <svg width="18" height="18" viewBox="0 0 24 24" fill="none" stroke="#fff" stroke-width="2"><path d="M5 3h4l2 5-2.5 1.5a11 11 0 0 0 6 6L16 13l5 2v4a2 2 0 0 1-2 2A17 17 0 0 1 3 5a2 2 0 0 1 2-2z"/></svg>
      34 600 481 372
    </div>
  </section>

</main>
</body>
</html>
```